Bref créative
Varneth Systems Stationery
Business card, envelops and letterhead
Bright & Fun-filled
Dorian Kelbrook
President & Chief Architect
418 W. Harrow Ln.
Kent, WA 98047
dorian.kelbrook@varneth.example
http://www.varneth.example
Please provide duplicate ai files in Illustrator 8.0 format and simlilar lower versions of any other files you provide as well as the originals
Logo only (without name)
Tag line:
"Providing Enterprise Business Solutions"
Original AI files

```html
<!DOCTYPE html>
<html lang="en">
<head>
<meta charset="utf-8">
<title>Varneth Systems Stationery</title>
<link href="https://fonts.googleapis.com/css2?family=Michroma&family=Open+Sans:wght@400;600;700&display=swap" rel="stylesheet">
<style>
  :root{
    --board:#3b3b3d;
    --navy:#1f2b6e;
    --navy-deep:#152058;
    --steel:#9ea3aa;
    --paper:#ffffff;
    --paper-shade:#e9eaec;
    --ink:#3c3f45;
    --ink-soft:#8a8e95;
  }
  html,body{margin:0;padding:0;}
  body{width:1200px;height:310px;overflow:hidden;background:var(--board);}
  .board{display:block;width:1200px;height:310px;}
  .brand{font-family:"Michroma",sans-serif;}
  .copy{font-family:"Open Sans",sans-serif;}
  .paper{fill:var(--paper);}
  .navy{fill:var(--navy);}
  .steel-line{fill:none;stroke:var(--steel);stroke-width:3;}
  .navy-line{fill:none;stroke:var(--navy);stroke-width:2;}
  .ink{fill:var(--ink);}
  .ink-soft{fill:var(--ink-soft);}
  .white{fill:#fff;}
  .shadow{filter:drop-shadow(0 2px 3px rgba(0,0,0,.45));}
</style>
</head>
<body>
<svg class="board" viewBox="0 0 1200 310" xmlns="http://www.w3.org/2000/svg">
  <defs>
    <g id="letter-wave">
      <path class="steel-line" d="M0,236 C50,214 108,250 156,226"/>
      <path class="navy" d="M0,246 C50,226 108,262 156,238 L156,279 L0,279 Z"/>
      <path fill="none" stroke="#fff" stroke-width="1.5" d="M0,258 C55,240 110,272 156,252"/>
    </g>
    <g id="mini-mark">
      <circle class="navy" cx="5" cy="5" r="5"/>
    </g>
  </defs>

  <!-- presentation title -->
  <g class="presentation-title">
    <circle cx="22" cy="44" r="13" class="white"/>
    <text class="brand white" x="42" y="50" font-size="17">VARNETH SYSTEMS</text>
    <text class="copy white" x="48" y="134" font-size="8">Stationery Concepts</text>
  </g>

  <!-- business card, front -->
  <g class="card card-front shadow" transform="translate(12,160)">
    <rect class="paper" width="137" height="72"/>
    <use href="#mini-mark" x="8" y="9"/>
    <text class="brand" fill="var(--navy)" x="22" y="17" font-size="6.5">VARNETH SYSTEMS</text>
    <text class="copy ink" x="8" y="36" font-size="5.5" font-weight="600">Dorian Kelbrook</text>
    <text class="copy ink-soft" x="8" y="43" font-size="4.2">President &amp; Chief Architect</text>
    <path class="steel-line" stroke-width="2" d="M0,56 C40,48 90,66 137,52"/>
    <path class="navy" d="M0,61 C40,53 90,71 137,57 L137,72 L0,72 Z"/>
  </g>

  <!-- business card, back -->
  <g class="card card-back shadow" transform="translate(156,160)">
    <rect class="navy" width="137" height="72"/>
    <text class="copy white" x="10" y="20" font-size="5.5" font-weight="600">Dorian Kelbrook</text>
    <text class="copy white" x="10" y="28" font-size="4.2">President &amp; Chief Architect</text>
    <text class="copy white" x="10" y="44" font-size="4">418 W. Harrow Ln.</text>
    <text class="copy white" x="10" y="50" font-size="4">Kent, WA 98047</text>
    <text class="copy white" x="10" y="56" font-size="4">dorian.kelbrook@varneth.example</text>
    <text class="copy white" x="10" y="62" font-size="4">(253) 555-0142</text>
  </g>

  <!-- business card, alternate front -->
  <g class="card card-alt shadow" transform="translate(12,240)">
    <rect class="paper" width="137" height="64"/>
    <circle class="navy" cx="20" cy="32" r="11"/>
    <text class="brand" fill="var(--navy)" x="37" y="35" font-size="6">VARNETH SYSTEMS</text>
    <text class="copy ink-soft" x="37" y="54" font-size="4">http://www.varneth.example</text>
  </g>

  <!-- business card, alternate back -->
  <g class="card card-alt-back shadow" transform="translate(156,240)">
    <rect class="navy" width="137" height="64"/>
    <text class="copy white" x="10" y="18" font-size="5.5" font-weight="600">Dorian Kelbrook</text>
    <text class="copy white" x="10" y="26" font-size="4.2">President &amp; Chief Architect</text>
    <text class="copy white" x="10" y="42" font-size="4">418 W. Harrow Ln., Kent, WA 98047</text>
    <text class="copy white" x="10" y="48" font-size="4">dorian.kelbrook@varneth.example</text>
    <text class="copy white" x="10" y="54" font-size="4">http://www.varneth.example</text>
  </g>

  <!-- letterhead A -->
  <g class="letterhead shadow" transform="translate(324,19)">
    <rect class="paper" width="156" height="279"/>
    <use href="#mini-mark" x="10" y="12"/>
    <text class="brand" fill="var(--navy)" x="24" y="20" font-size="5.5">VARNETH SYSTEMS</text>
    <g class="letter-address copy ink-soft" font-size="3.6" text-anchor="end">
      <text x="148" y="14">418 W. Harrow Ln.</text>
      <text x="148" y="19">Kent, WA 98047</text>
      <text x="148" y="24">(253) 555-0142</text>
    </g>
    <use href="#letter-wave"/>
    <text class="copy white" x="78" y="272" font-size="3.6" text-anchor="middle">http://www.varneth.example</text>
  </g>

  <!-- letterhead B -->
  <g class="letterhead shadow" transform="translate(492,19)">
    <rect class="paper" width="156" height="279"/>
    <use href="#mini-mark" x="30" y="12"/>
    <text class="brand" fill="var(--navy)" x="86" y="20" font-size="5.5" text-anchor="middle">VARNETH SYSTEMS</text>
    <text class="copy ink-soft" x="78" y="30" font-size="3.6" text-anchor="middle">Providing Enterprise Business Solutions</text>
    <use href="#letter-wave"/>
    <text class="copy white" x="78" y="272" font-size="3.6" text-anchor="middle">418 W. Harrow Ln. · Kent, WA 98047 · (253) 555-0142</text>
  </g>

  <!-- envelope front A -->
  <g class="envelope shadow" transform="translate(660,36)">
    <rect class="paper" width="175" height="120"/>
    <use href="#mini-mark" x="8" y="8"/>
    <text class="brand" fill="var(--navy)" x="22" y="16" font-size="6">VARNETH SYSTEMS</text>
    <text class="copy ink-soft" x="22" y="23" font-size="3.6">418 W. Harrow Ln., Kent, WA 98047</text>
    <path class="steel-line" d="M0,92 C55,78 115,104 175,84"/>
    <path class="navy" d="M0,100 C55,86 115,112 175,92 L175,120 L0,120 Z"/>
  </g>

  <!-- envelope front B -->
  <g class="envelope shadow" transform="translate(660,180)">
    <rect class="paper" width="175" height="113"/>
    <use href="#mini-mark" x="8" y="8"/>
    <text class="brand" fill="var(--navy)" x="22" y="16" font-size="6">VARNETH SYSTEMS</text>
    <text class="copy ink-soft" x="22" y="23" font-size="3.6">418 W. Harrow Ln., Kent, WA 98047</text>
    <path class="steel-line" d="M0,86 C55,72 115,98 175,78"/>
    <path class="navy" d="M0,94 C55,80 115,106 175,86 L175,113 L0,113 Z"/>
  </g>

  <!-- envelope back, grey -->
  <g class="envelope-back shadow" transform="translate(852,24)">
    <rect fill="var(--paper-shade)" width="324" height="72"/>
    <path fill="#6f7278" d="M0,0 L324,0 L162,40 Z"/>
    <circle class="white" cx="162" cy="22" r="7"/>
  </g>

  <!-- envelope back, navy flap -->
  <g class="envelope-back shadow" transform="translate(852,120)">
    <rect class="paper" width="324" height="72"/>
    <path class="navy-line" d="M0,72 L162,36 L324,72"/>
    <path class="navy" d="M0,0 L324,0 L162,44 Z"/>
    <circle class="white" cx="162" cy="24" r="7"/>
  </g>

  <!-- envelope front, plain -->
  <g class="envelope shadow" transform="translate(852,216)">
    <rect class="paper" width="324" height="67"/>
    <use href="#mini-mark" x="10" y="9"/>
    <text class="brand" fill="var(--navy)" x="24" y="17" font-size="6">VARNETH SYSTEMS</text>
    <path fill="none" stroke="#d4d6da" stroke-width="1" d="M0,67 L162,34 L324,67"/>
  </g>
</svg>
</body>
</html>
```